Surgical Conditions of the thyroid and parathyroid glands - a flyer for GPs

Hi there,

I am a thyroid surgeon trying to produce a bi-fold A4 flyer as a quick reference guide for general practitioners (family doctors). It needs to feel friendly and professional.

The text for the four "pages" can be found in the "thyroid flyer for design" document attached.

The front page should have:
- The title
- the photo with the patient having an ultrasound
- the photo of the asian woman with the enlarged thyroid gland
- possibly the photo of the blonde woman touching her neck

The inner two pages are predominantly text - I would love this to be presented in an easy to read, uncluttered format. There is a photo attached which demonstrates the parathyroid glands. This should be placed near the parathyroid text section if possible.

The back page is a brief bio of myself. It should have the profile pic attached.
It should have contact details, which I forgot to put in the word document. These details are:
Phone (03) 9482 5170 for all appointments
Consulting at:
18 Wattlebird Lane, Berwick, VIC 3806
hollowaymedicalteam.com.au
dorianpelsworth.com

The back page should also have the "Tarrow Care" and "Guild of Operators" logos.

If possible, all pages should have the "Holloway Medical Team" logo.

The whole feel could have a similar colour scheme to my group website (largely orange and green). Please see www.hollowaymedicalteam.com.au for examples.

Many thanks!

Target Market(s)

General practitioners (ie family doctors)

Industry/Entity Type

Medical And Science

Font styles to use
Sans Serif

Colors
33b8a4
f78f20

Requirements
Must have
• Contact details on the back, holloway medical team logo on front and back pages, Tarrow Care and Guild of Operators logo on the back.
Nice to have
• Other medical/surgical related images as you see fit - sorry to be so broad!!

```html
<!DOCTYPE html>
<html lang="en">
<head>
<meta charset="utf-8">
<title>Surgical Conditions of the Thyroid and Parathyroid Glands</title>
<link href="https://fonts.googleapis.com/css2?family=Montserrat:wght@500;600;700&family=Open+Sans:wght@400;600&display=swap" rel="stylesheet">
<style>
  :root{
    --teal:#16a49b;
    --green:#33b8a4;
    --orange:#f78f20;
    --pink:#e5488a;
    --grey:#676767;
    --ink:#444;
    --check:#777;
    --paper:#fbfbfb;
    --backdrop:#b4b4b4;
    --partner-blue:#2f5fa8;
    --partner-red:#9b2a2a;
  }
  *{margin:0;padding:0;box-sizing:border-box}
  html,body{width:986px;height:1200px;overflow:hidden;background:var(--backdrop)}
  .spread{position:absolute;left:23px;top:267px;width:940px;height:665px;display:flex;box-shadow:0 10px 30px rgba(0,0,0,.25)}
  .page{position:relative;width:470px;height:665px;overflow:hidden}
  .page svg.page-shapes{position:absolute;inset:0}
  .back-page{background:var(--paper);font-family:"Open Sans",sans-serif;color:var(--ink)}
  .front-page{background:var(--grey)}

  /* back page */
  .bio-photo{position:absolute;left:30px;top:58px;width:78px;height:96px;background:linear-gradient(160deg,#d9dde0,#8f959b)}
  .bio-heading{position:absolute;left:120px;top:50px;font:700 14px "Montserrat",sans-serif;color:var(--teal)}
  .bio-text{position:absolute;font-size:7.4px;line-height:1.45}
  .bio-intro{left:120px;top:72px;width:300px}
  .bio-intro p+p{margin-top:6px}
  .bio-body{left:30px;top:166px;width:392px}
  .bio-body p{margin-bottom:6px}
  .list-heading{font:700 11px "Montserrat",sans-serif;color:var(--teal);margin-bottom:5px}
  .condition-list{list-style:none;font-size:8px;line-height:1.6}
  .condition-list li,.contact-list li{display:flex;align-items:center;gap:5px}
  .condition-list svg,.contact-list svg{width:8px;height:8px;flex:none}
  .endocrine{position:absolute;left:30px;top:305px}
  .general{position:absolute;left:196px;top:305px}
  .contact{position:absolute;left:196px;top:430px;width:240px}
  .contact-heading{font:700 8px "Montserrat",sans-serif;color:var(--orange);line-height:1.3;margin-bottom:5px}
  .contact-list{list-style:none;font-size:8px;line-height:1.6}
  .partner-mark{position:absolute;top:530px;height:18px;border-radius:3px}
  .partner-one{left:196px;width:80px;background:var(--partner-blue)}
  .partner-two{left:296px;width:28px;background:var(--partner-red)}
  .back-logo{position:absolute;left:40px;top:560px;display:flex;align-items:center;gap:8px}
  .brand-dot{width:22px;height:22px;border-radius:50%;background:var(--green)}
  .brand-name{font:700 13px "Montserrat",sans-serif;color:var(--grey);line-height:1.1;text-transform:uppercase}

  /* front page */
  .cover-logo{position:absolute;left:308px;top:293px;width:124px;height:124px;display:flex;flex-direction:column;align-items:center;justify-content:center;gap:6px;text-align:center}
  .cover-logo .brand-dot{width:26px;height:26px}
  .cover-logo .brand-name{font-size:11px}
  .cover-title{position:absolute;left:36px;top:436px;width:410px;font-family:"Montserrat",sans-serif}
  .title-main{font-weight:700;font-size:25px;color:#fff;letter-spacing:.5px}
  .title-main small{font-size:20px;font-weight:600}
  .title-sub{font-weight:600;font-size:19px;color:var(--orange);margin-top:2px}
  .title-guide{font-weight:700;font-size:20.5px;color:var(--pink);margin-top:2px}
  .cover-web{margin-top:16px;padding:8px 0;border-top:1px solid rgba(255,255,255,.35);border-bottom:1px solid rgba(255,255,255,.35);font-weight:500;font-size:10px;letter-spacing:3px;color:#fff;text-align:center}
</style>
</head>
<body>
<main class="spread">

  <section class="page back-page">
    <svg class="page-shapes" viewBox="0 0 470 665" aria-hidden="true">
      <path d="M436 0H456V560A90 90 0 0 1 366 650H0V630H366A70 70 0 0 0 436 560Z" fill="var(--teal)"/>
      <path d="M456 0H470V665H0V650H366A90 90 0 0 0 456 560Z" fill="var(--grey)"/>
    </svg>

    <div class="bio-photo" role="img" aria-label="Portrait photo of the surgeon"></div>
    <h2 class="bio-heading">About Dorian:</h2>
    <div class="bio-text bio-intro">
      <p>Dorian is a graduate of Kestrel University (Bachelor of Medicine, Bachelor of Surgery, 2000) and has been a fellow of the Royal Australasian Guild of Operators since 2009.</p>
      <p>Dorian's surgical interests include benign and malignant disease of the thyroid and parathyroid glands, endoscopic trans-axillary and trans-oral thyroid surgery, and management of adrenal disease. He is the head of paediatric endocrine surgery at Tarrow Children's Hospital.</p>
    </div>
    <div class="bio-text bio-body">
      <p>He is happy to perform ultrasound-guided fine needle aspirates for most thyroid nodules as required, an advantage to patients in terms of time and cost.</p>
      <p>Away from medicine, Dorian is a classically-trained flautist and jazz saxophonist who plays with the Meridian Clinicians Ensemble. He is a keen follower of the Riverside football club and the Harbourside cricket club. Dorian travels to Sri Lanka regularly with projectHARBOR, a charity currently building a trauma centre on the east coast, a region affected by the Boxing Day tsunami and civil war.</p>
      <p>Dorian has public appointments with Tarrow Care (Clayton, Dandenong, Berwick and Moorabbin), Lindale Health and St Aldric's. He is an accredited specialist surgeon at The Grove, The Crescent, Northgate Richmond and St Ansel Private Hospitals.</p>
    </div>

    <div class="endocrine">
      <h3 class="list-heading">Endocrine conditions:</h3>
      <ul class="condition-list">
        <li><svg viewBox="0 0 10 10"><circle cx="5" cy="5" r="4.3" fill="none" stroke="var(--check)"/><path d="M3 5.2l1.4 1.4L7 3.8" fill="none" stroke="var(--check)"/></svg>Thyroid nodules</li>
        <li><svg viewBox="0 0 10 10"><circle cx="5" cy="5" r="4.3" fill="none" stroke="var(--check)"/><path d="M3 5.2l1.4 1.4L7 3.8" fill="none" stroke="var(--check)"/></svg>Thyroid cancer</li>
        <li><svg viewBox="0 0 10 10"><circle cx="5" cy="5" r="4.3" fill="none" stroke="var(--check)"/><path d="M3 5.2l1.4 1.4L7 3.8" fill="none" stroke="var(--check)"/></svg>Graves' disease/thyrotoxicosis</li>
        <li><svg viewBox="0 0 10 10"><circle cx="5" cy="5" r="4.3" fill="none" stroke="var(--check)"/><path d="M3 5.2l1.4 1.4L7 3.8" fill="none" stroke="var(--check)"/></svg>Multinodular goitre</li>
        <li><svg viewBox="0 0 10 10"><circle cx="5" cy="5" r="4.3" fill="none" stroke="var(--check)"/><path d="M3 5.2l1.4 1.4L7 3.8" fill="none" stroke="var(--check)"/></svg>Parathyroid disease</li>
        <li><svg viewBox="0 0 10 10"><circle cx="5" cy="5" r="4.3" fill="none" stroke="var(--check)"/><path d="M3 5.2l1.4 1.4L7 3.8" fill="none" stroke="var(--check)"/></svg>Adrenal disease</li>
      </ul>
    </div>

    <div class="general">
      <h3 class="list-heading">General surgical conditions:</h3>
      <ul class="condition-list">
        <li><svg viewBox="0 0 10 10"><circle cx="5" cy="5" r="4.3" fill="none" stroke="var(--check)"/><path d="M3 5.2l1.4 1.4L7 3.8" fill="none" stroke="var(--check)"/></svg>Laparoscopic cholecystectomy</li>
        <li><svg viewBox="0 0 10 10"><circle cx="5" cy="5" r="4.3" fill="none" stroke="var(--check)"/><path d="M3 5.2l1.4 1.4L7 3.8" fill="none" stroke="var(--check)"/></svg>Abdominal hernias (inguinal, umbilical, incisional)</li>
        <li><svg viewBox="0 0 10 10"><circle cx="5" cy="5" r="4.3" fill="none" stroke="var(--check)"/><path d="M3 5.2l1.4 1.4L7 3.8" fill="none" stroke="var(--check)"/></svg>Lipomas</li>
        <li><svg viewBox="0 0 10 10"><circle cx="5" cy="5" r="4.3" fill="none" stroke="var(--check)"/><path d="M3 5.2l1.4 1.4L7 3.8" fill="none" stroke="var(--check)"/></svg>Skin lesions</li>
        <li><svg viewBox="0 0 10 10"><circle cx="5" cy="5" r="4.3" fill="none" stroke="var(--check)"/><path d="M3 5.2l1.4 1.4L7 3.8" fill="none" stroke="var(--check)"/></svg>Carpal tunnel release</li>
        <li><svg viewBox="0 0 10 10"><circle cx="5" cy="5" r="4.3" fill="none" stroke="var(--check)"/><path d="M3 5.2l1.4 1.4L7 3.8" fill="none" stroke="var(--check)"/></svg>Ingrown toenails</li>
        <li><svg viewBox="0 0 10 10"><circle cx="5" cy="5" r="4.3" fill="none" stroke="var(--check)"/><path d="M3 5.2l1.4 1.4L7 3.8" fill="none" stroke="var(--check)"/></svg>Vasectomy</li>
      </ul>
    </div>

    <div class="contact">
      <p class="contact-heading">For more information about Holloway Medical Team<br>and our services please Contact :</p>
      <ul class="contact-list">
        <li><svg viewBox="0 0 10 10"><path d="M5 1L1 4.5h1.2V9h2V6.5h1.6V9h2V4.5H9Z" fill="var(--teal)"/></svg>Level 2, 18 Wattlebird Lane, Berwick, VIC 3806</li>
        <li><svg viewBox="0 0 10 10"><path d="M2.5 1l1.6 2-1 1.1a6 6 0 0 0 2.8 2.8l1.1-1L9 7.5 7.8 9C4.5 8.6 1.4 5.5 1 2.2Z" fill="var(--teal)"/></svg>(03) 9482 5170</li>
        <li><svg viewBox="0 0 10 10"><rect x="1" y="2" width="8" height="6" rx="1" fill="var(--teal)"/></svg>(03) 9482 5171</li>
        <li><svg viewBox="0 0 10 10"><circle cx="5" cy="5" r="4" fill="none" stroke="var(--teal)" stroke-width="1.4"/><path d="M1 5h8M5 1v8" stroke="var(--teal)" stroke-width=".8"/></svg>www.hollowaymedicalteam.com.au</li>
        <li><svg viewBox="0 0 10 10"><circle cx="5" cy="5" r="4" fill="none" stroke="var(--teal)" stroke-width="1.4"/><path d="M1 5h8M5 1v8" stroke="var(--teal)" stroke-width=".8"/></svg>www.dorianpelsworth.com</li>
      </ul>
    </div>
    <div class="partner-mark partner-one" aria-hidden="true"></div>
    <div class="partner-mark partner-two" aria-hidden="true"></div>

    <div class="back-logo">
      <span class="brand-dot"></span>
      <span class="brand-name">Holloway<br>Medical Team</span>
    </div>
  </section>

  <section class="page front-page">
    <svg class="page-shapes" viewBox="0 0 470 665">
      <defs>
        <linearGradient id="coverPhoto" x1="0" y1="0" x2="1" y2="1">
          <stop offset="0" stop-color="#c9a88f"/>
          <stop offset=".45" stop-color="#e8c8b4"/>
          <stop offset="1" stop-color="#c8c9d2"/>
        </linearGradient>
      </defs>
      <path d="M62 0H470V392H170A108 108 0 0 1 62 284Z" fill="var(--teal)"/>
      <g role="img" aria-label="Photo of a woman touching her neck">
        <path d="M86 0H470V372H178A92 92 0 0 1 86 280Z" fill="url(#coverPhoto)"/>
      </g>
      <circle cx="370" cy="355" r="66" fill="#fff" stroke="var(--teal)" stroke-width="11"/>
    </svg>

    <div class="cover-logo">
      <span class="brand-dot"></span>
      <span class="brand-name">Holloway<br>Medical Team</span>
    </div>

    <div class="cover-title">
      <h1 class="title-main">SURGICAL CONDITIONS <small>of</small></h1>
      <p class="title-sub">the Thyroid and Parathyroid Glands:</p>
      <p class="title-guide">A quick reference guide for GPs</p>
      <p class="cover-web">www.hollowaymedicalteam.com.au</p>
    </div>
  </section>

</main>
</body>
</html>
```